Long term design collaboration - mobile app design & web app design

We are looking for a talented mobile designer to help us improve our UI & UX for mobile app and web app.

The screens that need to be redesigned are attached.

There is potentially a lot more work in future design available for the successful candidate.
The successful candidate would have to take part in daily stand-up around 3 times per week.
The successful candidate would join a dev team
We are software company that does property management

```html
<!DOCTYPE html>
<html lang="en">
<head>
<meta charset="utf-8">
<title>Vantra – Dashboard</title>
<link href="https://fonts.googleapis.com/css2?family=Poppins:wght@400;500;600;700&display=swap" rel="stylesheet">
<style>
:root{
  --blue-dark:#0a5f9e;
  --blue:#0a7fc4;
  --blue-light:#11a3e4;
  --nav-active:#0b4f86;
  --ink:#1d2230;
  --muted:#8a8f9c;
  --line:#e3e6ec;
  --panel:#f1f3f7;
  --white:#ffffff;
  --green-a:#23c486;
  --green-b:#1b8fa8;
  --card2-a:#2f8fdc;
  --card2-b:#3552b3;
  --red:#e5484d;
  --chip-blue:#d9efff;
  --chip-red:#fde3e3;
}
*{box-sizing:border-box;margin:0;padding:0}
html,body{width:1200px;height:900px;overflow:hidden}
body{font-family:'Poppins',sans-serif;color:var(--ink);background:linear-gradient(135deg,var(--blue-dark),var(--blue) 50%,var(--blue-light))}
.app{position:relative;width:1200px;height:900px}
.sidebar{position:absolute;left:0;top:0;width:222px;height:900px;padding:22px 16px;color:var(--white)}
.brand{display:flex;align-items:center;gap:12px;margin-left:2px;font-weight:600;font-size:20px}
.brand-mark{width:28px;height:28px;border-radius:7px;background:var(--white)}
.new-report{margin-top:30px;height:46px;border-radius:23px;background:var(--white);color:var(--blue);display:flex;align-items:center;justify-content:center;gap:10px;font-size:13px;font-weight:500}
.new-report .plus{width:17px;height:19px;border-radius:3px;background:var(--blue);color:#fff;font-size:13px;line-height:19px;text-align:center}
.nav{margin-top:38px;list-style:none}
.nav li{height:44px;display:flex;align-items:center;gap:14px;padding:0 14px;font-size:11px;border-radius:8px;margin-bottom:3px}
.nav li.active{background:var(--nav-active);font-weight:600}
.nav svg{width:18px;height:18px;fill:none;stroke:#fff;stroke-width:1.8}
.logout{position:absolute;left:30px;bottom:110px;display:flex;align-items:center;gap:14px;font-size:11px}
.logout svg{width:18px;height:18px;fill:none;stroke:#fff;stroke-width:1.8}
.copyright{position:absolute;left:18px;bottom:60px;font-size:10px;line-height:16px;color:rgba(255,255,255,.75)}
.main{position:absolute;left:222px;top:18px;right:16px;bottom:18px;background:#fafbfc;border-radius:14px;padding:26px 28px}
.page-title{font-size:21px;font-weight:700}
.topbar{position:absolute;right:28px;top:24px;display:flex;align-items:center;gap:18px}
.bell{position:relative;width:18px;height:18px}
.bell svg{fill:#6b7280}
.bell .badge{position:absolute;top:-7px;right:-7px;width:13px;height:13px;border-radius:50%;background:var(--blue-light);color:#fff;font-size:8px;text-align:center;line-height:13px}
.user{display:flex;align-items:center;gap:8px}
.avatar{width:28px;height:28px;border-radius:50%;background:linear-gradient(135deg,#8a96a8,#c9a98a)}
.user-name{font-size:10px;font-weight:600;line-height:12px}
.user-role{font-size:8px;color:var(--muted)}
.caret{border:4px solid transparent;border-top-color:#9aa0ab;margin:4px 0 0 8px}
.content{display:flex;gap:42px;margin-top:26px}
.left{width:610px}
.balances{display:flex;gap:16px}
.balance{width:232px;height:126px;border-radius:8px;padding:20px;color:#fff;position:relative;overflow:hidden}
.balance.bank{background:linear-gradient(135deg,var(--green-a),var(--green-b))}
.balance.property{background:linear-gradient(135deg,var(--card2-a),var(--card2-b))}
.balance::after{content:"";position:absolute;right:-60px;top:-40px;width:190px;height:190px;border-radius:50%;background:rgba(255,255,255,.07)}
.balance-head{display:flex;align-items:center;gap:9px;font-size:12px;font-weight:600}
.balance-icon{width:24px;height:24px;border-radius:50%;background:rgba(255,255,255,.22)}
.balance-menu{position:absolute;right:14px;top:16px;font-size:12px;font-weight:700}
.balance-amount{margin-top:20px;font-size:18px;font-weight:600}
.balance-label{font-size:8px;letter-spacing:.3px;opacity:.85;margin-top:4px}
.section-title{font-size:17px;font-weight:600;margin:38px 0 16px}
.general{border:1px solid var(--line);border-radius:8px;background:#fff;padding:0 20px}
.stats{display:flex;padding:20px 0;border-bottom:1px solid var(--line)}
.stat{flex:1;display:flex;align-items:center;gap:11px}
.stat-icon{width:34px;height:34px;border-radius:50%;display:flex;align-items:center;justify-content:center}
.stat-icon svg{width:16px;height:16px}
.stat-value{font-size:12px;font-weight:600}
.stat-label{font-size:10px;color:var(--muted)}
.address{padding:28px 0 20px}
.compliance-head{display:flex;justify-content:space-between;align-items:center;margin:44px 0 14px}
.compliance-head .section-title{margin:0}
.view-all{border:1px solid var(--blue);border-radius:15px;height:29px;padding:0 14px;display:flex;align-items:center;gap:8px;font-size:10px;color:var(--blue);font-weight:500}
.checks{display:flex;gap:14px}
.check{flex:1;height:78px;background:#fff;border-radius:6px;box-shadow:0 1px 4px rgba(0,0,0,.07);padding:10px 12px 10px 24px;position:relative}
.check::before{content:"";position:absolute;left:12px;top:10px;bottom:10px;width:2px;background:var(--line)}
.check-name{font-size:10px;font-weight:600}
.check-sub{font-size:8px;color:var(--muted);margin-top:3px}
.chip{display:inline-block;margin-top:9px;font-size:7.5px;font-weight:600;padding:3px 6px;border-radius:3px}
.chip.info{background:var(--chip-blue);color:var(--blue)}
.chip.overdue{background:var(--chip-red);color:var(--red)}
.insurances{display:flex;gap:11px}
.insurance{width:93px;height:92px;border-radius:6px;border:1.5px solid var(--blue-light);background:#fff;position:relative;display:flex;flex-direction:column;align-items:center;justify-content:center;gap:14px;font-size:10px}
.insurance svg{width:22px;height:22px}
.insurance.off{border-color:var(--line);color:#c3c7cf}
.insurance .tick{position:absolute;top:7px;right:7px;width:13px;height:13px}
.setup{width:258px;height:640px;background:var(--panel);border-radius:8px;padding:14px 14px}
.setup-title{display:flex;align-items:center;gap:10px;font-size:12px;font-weight:600;padding:2px 0 14px;border-bottom:1px solid var(--line)}
.task{display:flex;align-items:center;gap:12px;margin-top:22px;height:36px}
.task-icon{width:20px;height:20px;border-radius:50%;background:#dbe9f6;flex:none}
.task-body{flex:1}
.task-name{font-size:10px;font-weight:500}
.task-progress{display:flex;align-items:center;gap:10px;margin-top:5px}
.bar{width:80px;height:3px;border-radius:2px;background:#dde1e8;position:relative}
.bar span{position:absolute;left:0;top:0;bottom:0;border-radius:2px;background:var(--blue-light)}
.pct{font-size:8px;color:var(--muted)}
.chev{width:10px;height:10px;fill:none;stroke:var(--blue);stroke-width:2}
</style>
</head>
<body>
<div class="app">
  <aside class="sidebar">
    <div class="brand"><span class="brand-mark"></span>Vantra</div>
    <div class="new-report"><span class="plus">+</span>New report</div>
    <ul class="nav">
      <li class="active"><svg viewBox="0 0 18 18"><rect x="2" y="2" width="14" height="5" fill="#fff"/><rect x="2" y="10" width="6" height="6" fill="#fff"/><rect x="10" y="10" width="6" height="6" fill="#fff"/></svg>Dashboard</li>
      <li><svg viewBox="0 0 18 18"><circle cx="6" cy="6" r="3"/><circle cx="13" cy="6" r="2.5"/><path d="M1 15c0-3 2.5-5 5-5s5 2 5 5M11 10c3 0 6 1.5 6 5"/></svg>User Directory</li>
      <li><svg viewBox="0 0 18 18"><rect x="2" y="3" width="14" height="11" rx="1"/><path d="M7 7l-2 2 2 2M11 7l2 2-2 2"/></svg>Switch Development</li>
      <li><svg viewBox="0 0 18 18"><rect x="2" y="4" width="14" height="10" rx="1.5"/><path d="M2 8h14"/></svg>Finances</li>
      <li><svg viewBox="0 0 18 18"><path d="M4 2h7l3 3v11H4z" fill="#fff"/><path d="M9 10h6M12 7l3 3-3 3" stroke="#0a7fc4"/></svg>Sending Letter</li>
      <li><svg viewBox="0 0 18 18"><circle cx="9" cy="9" r="3"/><circle cx="9" cy="9" r="6.5" stroke-dasharray="3 2"/></svg>Regular Services</li>
    </ul>
    <div class="logout"><svg viewBox="0 0 18 18"><path d="M2 9h9M8 6l3 3-3 3M12 3h4v12h-4"/></svg>Log out</div>
    <p class="copyright">Copyright © 2024. Vantra.<br>All Rights Reserved.</p>
  </aside>

  <main class="main">
    <h1 class="page-title">Dashboard</h1>
    <div class="topbar">
      <div class="bell"><svg viewBox="0 0 18 18"><path d="M9 2a5 5 0 0 0-5 5v5l-2 2h14l-2-2V7a5 5 0 0 0-5-5zM7 15a2 2 0 0 0 4 0z"/></svg><span class="badge">4</span></div>
      <div class="user">
        <div class="avatar" role="img" aria-label="User profile photo"></div>
        <div><div class="user-name">Dorian M.</div><div class="user-role">Account role</div></div>
        <span class="caret"></span>
      </div>
    </div>

    <div class="content">
      <section class="left">
        <div class="balances">
          <div class="balance bank">
            <div class="balance-head"><span class="balance-icon"></span>Quillfen Trust</div>
            <span class="balance-menu">⋮</span>
            <div class="balance-amount">$23,261,025.40</div>
            <div class="balance-label">AVAILABLE BANK BALANCE</div>
          </div>
          <div class="balance property">
            <div class="balance-head"><span class="balance-icon"></span>Property 101</div>
            <span class="balance-menu">⋮</span>
            <div class="balance-amount">$308,285,804.00</div>
            <div class="balance-label">AVAILABLE PROPERTY BALANCE</div>
          </div>
        </div>

        <h2 class="section-title">General</h2>
        <div class="general">
          <div class="stats">
            <div class="stat"><span class="stat-icon" style="background:#dcecf9"><svg viewBox="0 0 16 16" fill="#1d6fb8"><circle cx="8" cy="5" r="3"/><circle cx="4" cy="11" r="3"/><circle cx="12" cy="11" r="3"/></svg></span><div><div class="stat-value">85</div><div class="stat-label">Units</div></div></div>
            <div class="stat"><span class="stat-icon" style="background:#fde3e3"><svg viewBox="0 0 16 16" fill="none" stroke="#e5484d" stroke-width="1.6"><path d="M2 12a6 6 0 1 1 12 0"/><path d="M8 12l3-4"/></svg></span><div><div class="stat-value">£20</div><div class="stat-label">Section limit</div></div></div>
            <div class="stat"><span class="stat-icon" style="background:#fdefd9"><svg viewBox="0 0 16 16" fill="none" stroke="#f0a23a" stroke-width="1.6"><rect x="2" y="3" width="12" height="11" rx="1"/><path d="M2 7h12M5 1v3M11 1v3"/></svg></span><div><div class="stat-value">28 Jan 2025</div><div class="stat-label">Handover date</div></div></div>
          </div>
          <div class="address stat"><span class="stat-icon" style="background:#dff3e6"><svg viewBox="0 0 16 16" fill="#2a9d5c"><path d="M8 1a5 5 0 0 0-5 5c0 4 5 9 5 9s5-5 5-9a5 5 0 0 0-5-5zm0 7a2 2 0 1 1 0-4 2 2 0 0 1 0 4z"/></svg></span><div><div class="stat-value">42 Ashcombe Grove, Leeds, LS6 2QT</div><div class="stat-label">Address</div></div></div>
        </div>

        <div class="compliance-head">
          <h2 class="section-title">Compliance</h2>
          <span class="view-all"><b style="font-size:14px;font-weight:400">+</b>View all</span>
        </div>
        <div class="checks">
          <div class="check"><div class="check-name">Asbestos</div><div class="check-sub">N/A</div></div>
          <div class="check"><div class="check-name">Legionellas</div><div class="check-sub">-</div><span class="chip info">WHAT'S THIS ?</span></div>
          <div class="check"><div class="check-name">Gutters</div><div class="check-sub">N/A</div></div>
          <div class="check"><div class="check-name">Drains</div><div class="check-sub">12 December 2024</div><span class="chip overdue">▲ OVERDUE</span></div>
        </div>

        <h2 class="section-title" style="margin-top:36px">Insurances</h2>
        <div class="insurances">
          <div class="insurance"><svg class="tick" viewBox="0 0 13 13"><circle cx="6.5" cy="6.5" r="6.5" fill="#11a3e4"/><path d="M3.8 6.7l1.8 1.8 3.6-3.6" fill="none" stroke="#fff" stroke-width="1.4"/></svg><svg viewBox="0 0 22 22" fill="#1d5fa0"><path d="M4 2h14v18h-5v-4h-4v4H4z"/></svg>Buildings</div>
          <div class="insurance"><svg class="tick" viewBox="0 0 13 13"><circle cx="6.5" cy="6.5" r="6.5" fill="#11a3e4"/><path d="M3.8 6.7l1.8 1.8 3.6-3.6" fill="none" stroke="#fff" stroke-width="1.4"/></svg><svg viewBox="0 0 22 22" fill="#1d5fa0"><circle cx="11" cy="6" r="4"/><path d="M3 20c0-5 3.5-8 8-8s8 3 8 8z"/></svg>D &amp; O</div>
          <div class="insurance off"><svg viewBox="0 0 22 22" fill="#c3c7cf"><circle cx="8" cy="8" r="4"/><path d="M1 20c0-4 3-7 7-7s7 3 7 7z"/><circle cx="17" cy="6" r="3"/></svg>Engineering</div>
          <div class="insurance"><svg class="tick" viewBox="0 0 13 13"><circle cx="6.5" cy="6.5" r="6.5" fill="#11a3e4"/><path d="M3.8 6.7l1.8 1.8 3.6-3.6" fill="none" stroke="#fff" stroke-width="1.4"/></svg><svg viewBox="0 0 22 22" fill="none" stroke="#1d5fa0" stroke-width="2"><path d="M4 11a7 7 0 1 0 2-5"/><path d="M3 3v4h4M11 7v4l3 2"/></svg>Reinstatement</div>
          <div class="insurance off"><svg viewBox="0 0 22 22" fill="#c3c7cf"><circle cx="9" cy="6" r="4"/><path d="M2 20c0-5 3-8 7-8s7 3 7 8z"/><path d="M15 12l5-5 1 1-5 5z"/></svg>Terrorism</div>
        </div>
      </section>

      <aside class="setup">
        <div class="setup-title"><svg width="18" height="16" viewBox="0 0 18 16"><path d="M9 1l8 14H1z" fill="#e5484d"/><path d="M9 6v4M9 12v1" stroke="#fff" stroke-width="1.6"/></svg>Please complete basic setup</div>
        <div class="task"><span class="task-icon"></span><div class="task-body"><div class="task-name">Service Charge Schedules</div><div class="task-progress"><span class="bar"><span style="width:30%"></span></span><span class="pct">30% completed</span></div></div><svg class="chev" viewBox="0 0 10 10"><path d="M3 1l4 4-4 4"/></svg></div>
        <div class="task"><span class="task-icon"></span><div class="task-body"><div class="task-name">Service Charge Apportionment</div><div class="task-progress"><span class="bar"></span><span class="pct">0% completed</span></div></div><svg class="chev" viewBox="0 0 10 10"><path d="M3 1l4 4-4 4"/></svg></div>
        <div class="task"><span class="task-icon"></span><div class="task-body"><div class="task-name">Invite Residents and Leaseholders</div><div class="task-progress"><span class="bar"><span style="width:65%"></span></span><span class="pct">60% completed</span></div></div><svg class="chev" viewBox="0 0 10 10"><path d="M3 1l4 4-4 4"/></svg></div>
        <div class="task"><span class="task-icon"></span><div class="task-body"><div class="task-name">Connect Payment Provider</div><div class="task-progress"><span class="bar"></span><span class="pct">0% completed</span></div></div><svg class="chev" viewBox="0 0 10 10"><path d="M3 1l4 4-4 4"/></svg></div>
      </aside>
    </div>
  </main>
</div>
</body>
</html>
```